Business Card Design Project

Business and Appointment Card for Medical Practice. On back of card we would like to have: blank line for patient name, Mon-Fri each with a check box next to the day, blank line for appointment date, blank line for appointment time, with option to circle am or pm.

Target Market(s)

Professional Business Associates, as well as function as patient appointment cards (on back side of card)

Industry/Entity Type

Business

Colors

```html
<!DOCTYPE html>
<html lang="en">
<head>
<meta charset="utf-8">
<title>Birchwell Medical Group – Business &amp; Appointment Card</title>
<link rel="stylesheet" href="https://fonts.googleapis.com/css2?family=Open+Sans:wght@400;600;700&display=swap">
<style>
  :root {
    --page: #ecebe8;
    --paper: #ffffff;
    --brand-red: #8f1b22;
    --brand-green: #17693a;
    --label-green: #2d7a3f;
    --name-green: #3a9a4c;
    --dot-grey: #8a9a8d;
    --faint-art: #f3f1ef;
    --text-white: #ffffff;
    --shadow: rgba(0,0,0,0.18);
  }
  * { box-sizing: border-box; margin: 0; padding: 0; }
  html, body { width: 1200px; height: 784px; overflow: hidden; }
  body {
    background: var(--page);
    font-family: "Open Sans", Arial, sans-serif;
    position: relative;
  }
  .card {
    position: absolute;
    width: 548px;
    height: 313px;
    background: var(--paper);
    box-shadow: 0 4px 14px var(--shadow);
    overflow: hidden;
  }

  /* ---------- Appointment side ---------- */
  .card--appointment { left: 40px; top: 110px; }
  .appt-backdrop {
    position: absolute; left: 150px; top: 10px; width: 300px; height: 300px;
    border-radius: 50%;
    background: radial-gradient(circle, var(--faint-art) 0%, var(--faint-art) 60%, rgba(243,241,239,0) 72%);
  }
  .appt-title {
    position: absolute; left: 228px; top: 40px;
    color: var(--brand-red); font-size: 16px; font-weight: 600;
  }
  .dots {
    position: absolute; border-bottom: 2px dotted var(--dot-grey); height: 0;
  }
  .field-label {
    position: absolute; left: 34px;
    color: var(--label-green); font-size: 16px;
  }
  .weekdays {
    position: absolute; left: 336px; top: 120px;
    display: flex; gap: 6px; align-items: center;
    font-size: 10px; color: var(--label-green);
  }
  .weekday { display: flex; align-items: center; gap: 2px; }
  .checkbox {
    width: 14px; height: 14px; border: 1.5px solid var(--label-green); background: var(--paper);
  }
  .ampm {
    position: absolute; left: 352px; top: 156px;
    color: var(--label-green); font-size: 13px;
  }

  /* ---------- Business side ---------- */
  .card--business { left: 612px; top: 360px; }
  .card-waves { position: absolute; inset: 0; }
  .brand {
    position: absolute; left: 0; top: 34px; width: 548px;
    display: flex; flex-direction: column; align-items: center; gap: 10px;
  }
  .brand-dot { width: 56px; height: 56px; border-radius: 50%; background: var(--brand-green); }
  .brand-name {
    color: var(--brand-red); font-size: 24px; font-weight: 700; letter-spacing: 0.5px;
  }
  .person {
    position: absolute; left: 40px; top: 240px; width: 214px; text-align: right;
  }
  .person-name { color: var(--name-green); font-size: 19px; line-height: 1.1; }
  .person-role { color: var(--text-white); font-size: 12px; font-weight: 600; margin-top: 2px; }
  .divider {
    position: absolute; left: 272px; top: 214px; width: 1px; height: 84px; background: var(--text-white);
  }
  .contact-list {
    position: absolute; left: 284px; top: 212px; list-style: none;
    color: var(--text-white); font-size: 13px; line-height: 21px;
  }
  .contact-list li { display: flex; align-items: center; gap: 6px; }
  .contact-list svg { width: 12px; height: 12px; fill: var(--text-white); flex: none; }
</style>
</head>
<body>

  <section class="card card--appointment" aria-label="Appointment card">
    <div class="appt-backdrop" role="img" aria-label="Faint tree illustration behind the form"></div>
    <div class="appt-title">Appointment</div>
    <div class="dots" style="left:200px; top:70px; width:314px;"></div>

    <div class="field-label" style="top:114px;">Name :</div>
    <div class="dots" style="left:100px; top:133px; width:228px;"></div>
    <div class="weekdays">
      <span class="weekday">Mon <span class="checkbox"></span></span>
      <span class="weekday">Tue <span class="checkbox"></span></span>
      <span class="weekday">Wed <span class="checkbox"></span></span>
      <span class="weekday">Thu <span class="checkbox"></span></span>
      <span class="weekday">Fri <span class="checkbox"></span></span>
    </div>

    <div class="field-label" style="top:148px;">Date :</div>
    <div class="dots" style="left:100px; top:167px; width:240px;"></div>
    <div class="ampm">am / pm</div>

    <div class="field-label" style="top:182px;">Time :</div>
    <div class="dots" style="left:100px; top:201px; width:120px;"></div>
  </section>

  <section class="card card--business" aria-label="Business card">
    <svg class="card-waves" viewBox="0 0 548 313" preserveAspectRatio="none" aria-hidden="true">
      <path d="M0,196 C130,236 280,212 548,116 L548,313 L0,313 Z" fill="var(--brand-green)"/>
      <path d="M0,212 C130,254 290,230 548,136 L548,313 L0,313 Z" fill="var(--brand-red)"/>
    </svg>

    <div class="brand">
      <span class="brand-dot"></span>
      <span class="brand-name">Birchwell Medical Group</span>
    </div>

    <div class="person">
      <div class="person-name">Daniel Carter</div>
      <div class="person-role">Manager</div>
    </div>
    <div class="divider"></div>

    <ul class="contact-list">
      <li><svg viewBox="0 0 24 24"><path d="M6.6 10.8a15.1 15.1 0 0 0 6.6 6.6l2.2-2.2c.3-.3.7-.4 1-.2 1.1.4 2.300.6 3.6.6.6 0 1 .4 1 1V20c0 .6-.4 1-1 1A17 17 0 0 1 3 4c0-.6.4-1 1-1h3.5c.6 0 1 .4 1 1 0 1.3.2 2.5.6 3.6.1.3 0 .7-.2 1z"/></svg>555-210-4837</li>
      <li><svg viewBox="0 0 24 24"><path d="M12 2a10 10 0 1 0 0 20 10 10 0 0 0 0-20zm6.9 6h-3a15.7 15.7 0 0 0-1.4-3.6A8 8 0 0 1 18.9 8zM12 4c.8 1.2 1.5 2.5 1.9 4h-3.8c.4-1.5 1.1-2.8 1.9-4zM4.3 14a8 8 0 0 1 0-4h3.4a16.5 16.5 0 0 0 0 4zm.8 2h3c.3 1.3.8 2.5 1.4 3.6A8 8 0 0 1 5.1 16zm3-8h-3a8 8 0 0 1 4.4-3.6C8.9 5.5 8.4 6.7 8.1 8zM12 20c-.8-1.2-1.5-2.5-1.9-4h3.8c-.4 1.5-1.1 2.8-1.9 4zm2.3-6H9.7a14.7 14.7 0 0 1 0-4h4.6a14.7 14.7 0 0 1 0 4zm.3 5.6c.6-1.1 1.1-2.3 1.4-3.6h3a8 8 0 0 1-4.4 3.6zm1.7-5.6a16.5 16.5 0 0 0 0-4h3.4a8 8 0 0 1 0 4z"/></svg>www.birchwellclinic.com</li>
      <li><svg viewBox="0 0 24 24"><path d="M20 4H4a2 2 0 0 0-2 2v12c0 1.1.9 2 2 2h16a2 2 0 0 0 2-2V6a2 2 0 0 0-2-2zm0 4-8 5-8-5V6l8 5 8-5z"/></svg>info@birchwellclinic.com</li>
      <li><svg viewBox="0 0 24 24"><path d="M10 20v-6h4v6h5v-8h3L12 3 2 12h3v8z"/></svg>48 Linden Avenue Westbrook</li>
    </ul>
  </section>

</body>
</html>
```